Thornwell Building Company - advertisement poster

I am looking to print some canvas signs to advertise my general contracting company, Thornwell Building Company. The sign will measure 6' long x 3' high so the size should match that ratio. I already have a logo icon, which is the Letter 'A' and some trees that I would like to incorporate, see attached. I would also like the to have the following information listed:
1) phone number: 472-318-6095
2) email: thornwellbuildingcompany@mailvistra.net
3) website: thornwellbuildingcompany.com
4) Lic#5386204
5) I want to use this text: "BUILD WITH THE T-CREW!"

The ad should be relatively simple and clean. Black and Green are my company colors. I am open to creative ideas!

Target Market(s)

People looking to renovate their homes

Industry/Entity Type

Construction

Colors
59FF00
82FF00
B8FF75
E3FFCB
F4FFEA

Requirements
Must have
• Must have my company logo
Should not have
• No photos or complex graphics

```html
<!DOCTYPE html>
<html lang="en">
<head>
<meta charset="utf-8">
<title>Thornwell Building Company – Sign</title>
<link rel="stylesheet" href="https://fonts.googleapis.com/css2?family=Montserrat:wght@300;400;600;700;800&display=swap">
<style>
  :root {
    --backdrop: #dedcdd;
    --sign: #1b1b1b;
    --green: #5cb832;
    --white: #ffffff;
    --photo-light: #d9d9d9;
    --photo-mid: #6e6e6e;
  }
  * { margin: 0; padding: 0; box-sizing: border-box; }
  html, body {
    width: 700px; height: 1200px; overflow: hidden;
    background: var(--backdrop);
    font-family: "Montserrat", sans-serif;
  }
  .sign {
    position: absolute; left: 10px; top: 430px;
    width: 680px; height: 340px;
    background: var(--sign);
    overflow: hidden;
    color: var(--white);
  }
  .brand {
    position: absolute; top: 22px; left: 0; width: 390px;
    display: flex; align-items: center; justify-content: center; gap: 12px;
  }
  .brand-dot {
    flex: none; width: 30px; height: 30px; border-radius: 50%;
    background: var(--green);
  }
  .brand-name {
    font-weight: 700; font-size: 18px; letter-spacing: 0.5px;
    line-height: 1.2; text-transform: uppercase;
  }
  .headline {
    position: absolute; top: 100px; left: 0; width: 390px;
    text-align: center; font-weight: 300; font-size: 32px;
    letter-spacing: 0.5px; line-height: 1;
  }
  .crew-box {
    position: absolute; top: 148px; left: 87px;
    width: 216px; height: 56px;
    border: 2px solid var(--green); border-radius: 8px;
    display: flex; align-items: center; justify-content: center;
    color: var(--green); font-weight: 800; font-size: 40px; letter-spacing: -1px;
  }
  .photo-area {
    position: absolute; left: 410px; top: 0;
    width: 270px; height: 250px;
    background:
      linear-gradient(to bottom, rgba(27,27,27,0) 50%, var(--sign) 100%),
      linear-gradient(to right, var(--sign) 0%, rgba(27,27,27,0) 25%),
      linear-gradient(135deg, var(--photo-light) 0%, var(--photo-mid) 45%, #2a2a2a 100%);
  }
  .contact-frame {
    position: absolute; left: 0; top: 250px; width: 680px; height: 90px;
  }
  .phone {
    position: absolute; top: 252px; left: 0; width: 100%;
    display: flex; align-items: center; justify-content: center; gap: 9px;
    font-weight: 600; font-size: 26px; line-height: 34px;
  }
  .phone-icon { width: 28px; height: 28px; }
  .licence {
    position: absolute; top: 290px; left: 0; width: 100%;
    text-align: center; font-weight: 400; font-size: 14px; line-height: 18px;
  }
  .online {
    position: absolute; top: 314px; left: 0; width: 100%;
    display: flex; justify-content: center; gap: 22px;
    font-weight: 400; font-size: 13px; line-height: 18px; letter-spacing: 0.3px;
  }
  .online strong { color: var(--green); font-weight: 700; }
</style>
</head>
<body>
  <main class="sign">
    <header class="brand">
      <span class="brand-dot" aria-hidden="true"></span>
      <p class="brand-name">Thornwell<br>Building Company</p>
    </header>

    <h1 class="headline">BUILD WITH THE</h1>
    <div class="crew-box">T-CREW</div>

    <div class="photo-area" role="img" aria-label="Black and white photo of curved concrete building balconies"></div>

    <svg class="contact-frame" viewBox="0 250 680 90" aria-hidden="true">
      <polyline points="0,270 150,270 175,300 265,300" fill="none" stroke="#5cb832" stroke-width="1.5"/>
      <polyline points="415,300 505,300 530,270 680,270" fill="none" stroke="#5cb832" stroke-width="1.5"/>
    </svg>

    <div class="phone">
      <svg class="phone-icon" viewBox="0 0 40 40" aria-hidden="true">
        <circle cx="20" cy="20" r="20" fill="#5cb832"/>
        <path d="M14 10c1-.6 2-.4 2.6.6l2 3.4c.5.9.3 1.9-.5 2.5l-1.5 1.1c1 2.3 2.7 4 5 5l1.1-1.5c.6-.8 1.6-1 2.5-.5l3.4 2c1 .6 1.2 1.6.6 2.6l-1.4 2.2c-.6 1-1.8 1.4-2.9 1.1C18.6 27 13 21.4 11 15.1c-.3-1.1.1-2.3 1.1-2.9z" fill="#1b1b1b"/>
      </svg>
      <span>472-318-6095</span>
    </div>
    <p class="licence">Lic#5386204</p>
    <p class="online">
      <span class="website">www.<strong>thornwellbuildingcompany</strong>.com</span>
      <span class="email">thornwellbuildingcompany@mailvistra.net</span>
    </p>
  </main>
</body>
</html>
```